Storage Company Newsletter

We need a design for a newsletter for our company Vaultrix, a digital and physical asset storage company .The newsletter will be informative and educational covering tips on secure storage of personal documents and items both at home and at the work place. Rest easy with Vaultrix is our mantra. We have a pre-existing trademark & logo. Colors are blue and green. We can share the cmyk/rgb color information and background is grey.

Target Market(s)

Mass market – Middle to High income individuals

Industry/Entity Type

Digital

Font styles to use
Sans Serif

Colors
0393ce
00a88f
edf2f7

Requirements
Must have
• The newsletter linked to a CMS. In HTML5; Mail-chimp integration readable on Gmail, Yahoo, Hotmail and Outlook
Nice to have
• Sections of the newsletter are:
• Cover story
• News Flash
• Mwanachi Perspective
• Spotlight on the Counties
• CEO's Corner
• Tips and Helpful Information
• Important Dates and Events

```html
<!DOCTYPE html>
<html lang="en">
<head>
<meta charset="utf-8">
<title>Vaultrix Newsletter</title>
<link href="https://fonts.googleapis.com/css2?family=Figtree:wght@300;400;600;700&family=Open+Sans:wght@400;600&display=swap" rel="stylesheet">
<style>
  :root {
    --page: #f3f4f2;
    --dark: #333333;
    --ink: #111111;
    --body: #6b6b6b;
    --blue: #29a9e1;
    --brand-blue: #0393ce;
    --teal: #00997f;
    --purple: #4a3a8c;
    --rule: #dddddd;
    --foot-line: #6a6a6a;
    --white: #ffffff;
  }
  * { box-sizing: border-box; margin: 0; padding: 0; }
  html, body { width: 825px; height: 1200px; overflow: hidden; background: var(--page); }
  body { font-family: "Open Sans", Arial, sans-serif; }
  .stage { width: 800px; height: 1164px; position: relative; transform: scale(1.03125); transform-origin: 0 0; }
  .abs { position: absolute; }
  .lines { white-space: nowrap; }

  /* header */
  .masthead { left: 80px; top: 0; width: 640px; height: 71px; background: var(--dark); overflow: hidden; }
  .masthead .corner { left: 0; top: 0; width: 0; height: 0; border-top: 71px solid var(--teal); border-right: 60px solid transparent; }
  .brand { left: 36px; top: 18px; display: flex; align-items: center; gap: 12px; }
  .brand-mark { width: 32px; height: 32px; background: var(--brand-blue); }
  .brand-name { font-family: "Figtree", sans-serif; font-weight: 700; font-size: 27px; letter-spacing: 1px; color: var(--brand-blue); }
  .web-view { right: 31px; top: 28px; display: flex; align-items: center; gap: 5px; font-family: "Figtree", sans-serif; font-size: 12px; color: #bcbcbc; }

  /* hero */
  .hero { left: 80px; top: 71px; width: 640px; height: 251px; background: linear-gradient(135deg, #dedede 0%, #d3d3d3 100%); }
  .hero h1 { left: 36px; top: 42px; font-family: "Figtree", sans-serif; font-weight: 300; font-size: 26px; line-height: 30px; color: var(--ink); white-space: nowrap; }
  .hero h1 strong { font-weight: 700; }
  .hero p { left: 36px; top: 109px; font-family: "Figtree", sans-serif; font-size: 12px; line-height: 15.5px; color: #444; }
  .pill { display: flex; align-items: center; justify-content: center; gap: 5px; background: var(--white); border-radius: 12px; font-family: "Figtree", sans-serif; font-weight: 700; font-size: 9.5px; color: var(--brand-blue); }
  .hero .pill { left: 36px; top: 192px; width: 100px; height: 23px; }
  .hero-art { left: 370px; top: 24px; width: 230px; height: 210px; border-radius: 8px; background: radial-gradient(circle at 55% 75%, #8fd3f2 0%, #b9dfef 30%, rgba(215,215,215,0) 70%); }

  /* articles */
  .article h2 { position: absolute; left: 90px; font-family: "Figtree", sans-serif; font-weight: 700; font-size: 18px; line-height: 24px; color: var(--ink); white-space: nowrap; }
  .thumb { position: absolute; left: 92px; width: 111px; height: 111px; }
  .thumb-servers { background: linear-gradient(90deg, #141414 0%, #3b3e45 45%, #9aa0ab 70%, #202226 100%); }
  .thumb-folder { background: #d6ebf7; }
  .thumb-keys { background: linear-gradient(150deg, #f4f4f4 0%, #c9ccd0 55%, #2a9ad6 100%); }
  .article p { position: absolute; left: 218px; font-size: 10.4px; line-height: 18px; color: var(--body); white-space: nowrap; }
  .read-btn { position: absolute; left: 216px; width: 122px; height: 22px; border-radius: 11px; background: #000; color: var(--white); font-family: "Figtree", sans-serif; font-weight: 600; font-size: 10.5px; display: flex; align-items: center; padding-left: 13px; gap: 14px; }
  .divider { position: absolute; left: 90px; width: 390px; height: 1px; background: var(--rule); }

  /* sidebar */
  .perspective { left: 529px; top: 348px; width: 191px; height: 202px; background: var(--teal); }
  .perspective .title { left: 0; top: 16px; width: 191px; text-align: center; font-family: "Figtree", sans-serif; font-weight: 300; font-size: 20px; letter-spacing: 1.5px; color: var(--purple); }
  .perspective .ribbon { left: 46px; top: 41px; width: 106px; height: 16px; background: var(--purple); color: var(--white); font-family: "Figtree", sans-serif; font-weight: 700; font-size: 10px; letter-spacing: 1px; text-align: center; line-height: 16px; }
  .perspective p { left: 23px; top: 63px; font-size: 10px; line-height: 13.5px; color: var(--white); white-space: nowrap; }
  .perspective .pill { left: 24px; top: 160px; width: 99px; height: 22px; color: var(--teal); }

  .side-panel { left: 529px; top: 563px; width: 191px; height: 421px; background: var(--white); border: 1px solid var(--rule); }
  .side-panel .split { left: 0; top: 204px; width: 189px; height: 1px; background: var(--rule); }
  .tag { position: absolute; left: 18px; width: 154px; height: 29px; border-radius: 3px; background: var(--blue); color: var(--white); font-family: "Figtree", sans-serif; font-weight: 600; font-size: 15px; display: flex; align-items: center; gap: 10px; padding-left: 10px; }
  .side-panel p { position: absolute; left: 19px; width: 153px; font-size: 9.9px; letter-spacing: .1px; line-height: 13px; color: var(--body); text-align: justify; }

  /* footer */
  .footer { left: 81px; top: 1017px; width: 639px; height: 147px; background: var(--dark); border-top: 5px solid var(--teal); }
  .foot-box { position: absolute; top: 20px; width: 190px; height: 71px; border: 1px solid var(--foot-line); display: flex; align-items: center; justify-content: center; gap: 10px; color: #d0d0d0; font-family: "Figtree", sans-serif; font-size: 13px; }
  .connect { flex-direction: column; gap: 6px; font-size: 9px; letter-spacing: .3px; }
  .socials { display: flex; gap: 10px; }
  .socials span { width: 28px; height: 28px; background: #5d5d5d; display: block; }
  .legal { position: absolute; left: 0; width: 639px; text-align: center; font-family: "Figtree", sans-serif; font-size: 10px; line-height: 13px; color: #8d8d8d; }
</style>
</head>
<body>
<div class="stage">

  <header class="masthead abs">
    <div class="corner abs"></div>
    <div class="brand abs"><span class="brand-mark"></span><span class="brand-name">VAULTRIX</span></div>
    <div class="web-view abs">
      <svg width="14" height="14" viewBox="0 0 14 14"><circle cx="7" cy="7" r="6" fill="none" stroke="#bcbcbc" stroke-width="1.6"/><path d="M4 7h5M7 4.5 9.5 7 7 9.5" fill="none" stroke="#bcbcbc" stroke-width="1.6"/></svg>
      View in Web Browser
    </div>
  </header>

  <section class="hero abs">
    <h1 class="abs">Caring for<br><strong>Valuable Documents</strong></h1>
    <p class="abs lines">Valuable documents include a wide range<br>of items such as landtitle deeds, certifi-<br>cates, letters, photographs, newspaper<br>cuttings andmemorabilia.</p>
    <a class="pill abs">LEARN MORE <svg width="6" height="7" viewBox="0 0 6 7"><path d="M0 0 6 3.5 0 7z" fill="#0393ce"/></svg></a>
    <div class="hero-art abs" role="img" aria-label="Illustration of a locked blue folder with bursting doodle icons above it"></div>
  </section>

  <article class="article">
    <h2 style="top:347px">Phasellus sit amet augue scelerisque, mollis<br>tortor in, viverra nulla.</h2>
    <div class="thumb thumb-servers" style="top:411px" role="img" aria-label="Photo of a data centre aisle lined with server racks"></div>
    <p style="top:408px">Phasellus lacinia neque orci, non luctus tellus<br>sollicitudin volutpat. Nunc dapibus quam id accum-<br>san adipiscing. Morbi a neque egestas, volutpat<br>dolor in, bibendum odio. Ut et tempor nisi, non</p>
    <a class="read-btn" style="top:494px">Read Full Article <svg width="7" height="8" viewBox="0 0 7 8"><path d="M0 0 7 4 0 8z" fill="#fff"/></svg></a>
  </article>
  <div class="divider" style="top:551px"></div>

  <article class="article">
    <h2 style="top:575px">Curabitur tincidunt neque non justo vehicula<br>in sollicitudin nibh dictum.</h2>
    <div class="thumb thumb-folder" style="top:639px" role="img" aria-label="Illustration of a folder with a key"></div>
    <p style="top:636px">Integer pellentesque augue nec blandit ultrices.<br>Proin vel purus vel libero dignissim mollis vel id<br>lorem. Sed suscipit diam eget magna lacinia, biben-<br>dum tempus odio sollicitudin.</p>
    <a class="read-btn" style="top:722px">Read Full Article <svg width="7" height="8" viewBox="0 0 7 8"><path d="M0 0 7 4 0 8z" fill="#fff"/></svg></a>
  </article>
  <div class="divider" style="top:779px"></div>

  <article class="article">
    <h2 style="top:806px">Maecenas vel purus gravida, dignissim quam<br>nec, pharetra lacus.</h2>
    <div class="thumb thumb-keys" style="top:870px" role="img" aria-label="Photo of a keyboard with a blue archive key"></div>
    <p style="top:867px">Phasellus lacinia neque orci, non luctus tellus<br>sollicitudin volutpat. Nunc dapibus quam id accum-<br>san adipiscing. Morbi a neque egestas, volutpat<br>dolor in, bibendum odio. Ut et tempor nisi, non</p>
    <a class="read-btn" style="top:953px">Read Full Article <svg width="7" height="8" viewBox="0 0 7 8"><path d="M0 0 7 4 0 8z" fill="#fff"/></svg></a>
  </article>

  <aside class="perspective abs">
    <div class="title abs">COMMUNITY</div>
    <div class="ribbon abs">VIEWPOINT</div>
    <p class="abs">Phasellus lacinia neque<br>orci, non luctus tellus<br>sollicitudin volutpat. Nunc<br>dapibus quam id accumsan<br>adipiscing. Morbi a neque<br>egestas, volutpat dolor in,</p>
    <a class="pill abs">LEARN MORE <svg width="6" height="7" viewBox="0 0 6 7"><path d="M0 0 6 3.5 0 7z" fill="#00997f"/></svg></a>
  </aside>

  <aside class="side-panel abs">
    <div class="tag" style="top:21px">
      <svg width="17" height="17" viewBox="0 0 17 17"><rect x="1" y="3" width="15" height="13" fill="none" stroke="#fff" stroke-width="1.6"/><path d="M1 7h15M5 1v4M12 1v4" stroke="#fff" stroke-width="1.6"/></svg>
      News Flash
    </div>
    <p style="top:64px">Phasellus lacinia neque orci, non luctus tellus sollicitudin volutpat. Nunc dapibus quam id accumsan adipiscing.<br><br>Morbi a neque egestas, volutpat dolor in, bibendum odio. Ut et tempor nisi, non auctor velit.</p>
    <div class="split abs"></div>
    <div class="tag" style="top:230px">
      <svg width="17" height="17" viewBox="0 0 17 17"><rect x="1" y="3" width="12" height="13" fill="none" stroke="#fff" stroke-width="1.6"/><path d="M6 11 15 2" stroke="#fff" stroke-width="2"/></svg>
      CEO Corner
    </div>
    <p style="top:273px">Fusce et lectus eu ipsum biben-dum consectetur. Aliquam id mi ut nulla malesuada varius.Sed blandit quam ultricies lectus euismod imperdiet.<br><br>Donec et massa vel nisi posuere porttitor vitae eget turpis. Sed ac tellus ac magna.</p>
  </aside>

  <footer class="footer abs">
    <div class="foot-box connect" style="left:19px">
      CONNECT WITH US:
      <div class="socials">
        <span role="img" aria-label="Video channel"></span>
        <span role="img" aria-label="Professional network"></span>
        <span role="img" aria-label="Social page"></span>
        <span role="img" aria-label="Microblog"></span>
      </div>
    </div>
    <div class="foot-box" style="left:224px">
      <svg width="22" height="16" viewBox="0 0 22 16"><rect width="22" height="16" rx="2" fill="#e0e0e0"/><path d="M1 1l10 8 10-8" fill="none" stroke="#333" stroke-width="1.6"/></svg>
      info@vaultrix.org
    </div>
    <div class="foot-box" style="left:427px">
      <svg width="22" height="22" viewBox="0 0 22 22"><circle cx="11" cy="11" r="10" fill="none" stroke="#e0e0e0" stroke-width="1.6"/><path d="M7 5.5c-1 1-1 3 1.5 6s5 4 6.5 3l1-1.5-2.5-1.8-1.2 1c-1-.4-2.5-2-3-3l1-1.2L8.5 5z" fill="#e0e0e0"/></svg>
      +254700482913
    </div>
    <div class="legal" style="top:111px">Unsubscribe or change email preferences I Privacy Policy I Terms of Service<br>Copyright © Vaultrix.org 2014. All rights reserved</div>
  </footer>

</div>
</body>
</html>
```